Veterinary Business cards

Redesign Business Card

Information needed on Card:
Hours: Mon-Fri: 4pm -10PM; Sat- Sun- 10 AM- 5PM
Help@bayfernvet.com
www.bayfernvet.com
555-718-2946
4173 SE 19th Ave. okc, ok 73958
*No appointment necessary*

Optional:
Our tag line is "We're here when you need us" - If it fits on the cards.

```html
<!DOCTYPE html>
<html lang="en">
<head>
<meta charset="utf-8">
<title>Bayfern Vet Urgent Care – Business Cards</title>
<link href="https://fonts.googleapis.com/css2?family=Marcellus&family=Roboto:wght@400;500&family=Roboto+Condensed:wght@700&family=Patrick+Hand&display=swap" rel="stylesheet">
<style>
  :root {
    --bg: #2a2a2a;
    --card: #eeeeee;
    --card-edge: #e2e2e2;
    --navy: #1c3961;
    --orange: #c2731d;
    --band-text: #f2f2f2;
  }
  * { margin: 0; padding: 0; box-sizing: border-box; }
  html, body { width: 1200px; height: 1138px; overflow: hidden; background: var(--bg); }
  .canvas { position: relative; width: 1200px; height: 1138px; }

  .card {
    position: absolute;
    width: 622px; height: 375px;
    border-radius: 16px;
    background: linear-gradient(160deg, #f4f4f4 0%, var(--card) 55%, var(--card-edge) 100%);
    overflow: hidden;
    font-family: "Roboto", Arial, sans-serif;
  }
  .card-front { left: 274px; top: 186px; }
  .card-back  { left: 276px; top: 608px; }

  .brand-name {
    font-family: "Marcellus", Georgia, serif;
    color: var(--navy);
    font-weight: 400;
    text-align: center;
    line-height: 1;
  }
  .card-front .brand-name {
    position: absolute; left: 0; right: 0; top: 122px;
  }
  .card-front .brand-title { font-size: 56px; letter-spacing: 1px; }
  .card-front .brand-sub { font-size: 21px; letter-spacing: 3px; margin-top: 10px; }

  .walk-in-band {
    position: absolute; left: 0; right: 0; top: 280px; height: 34px;
    background: linear-gradient(90deg, var(--navy) 0%, #3a3d44 35%, #5a4a38 65%, var(--orange) 100%);
    color: var(--band-text);
    font-size: 16px; letter-spacing: 0.2px;
    display: flex; align-items: center; justify-content: center;
  }
  .hours {
    position: absolute; left: 0; right: 0; top: 327px;
    text-align: center; font-size: 16.5px; color: var(--navy);
  }
  .hours .label { color: var(--orange); }
  .hours .divider { color: var(--orange); margin: 0 6px; font-weight: 500; }

  .doctor-name {
    position: absolute; left: 36px; top: 62px;
    font-family: "Roboto Condensed", "Arial Narrow", sans-serif;
    font-weight: 700; font-size: 24px; color: var(--orange);
  }
  .card-back .brand-name {
    position: absolute; right: 34px; top: 70px; width: 280px;
  }
  .card-back .brand-title { font-size: 40px; letter-spacing: 1px; }
  .card-back .brand-sub { font-size: 15px; letter-spacing: 2.5px; margin-top: 6px; }

  .contact-list { position: absolute; left: 36px; top: 145px; list-style: none; }
  .contact-list li {
    display: flex; align-items: center; height: 24px;
    font-size: 16px; color: var(--navy);
  }
  .contact-list svg { width: 15px; height: 15px; margin-right: 12px; fill: var(--orange); }
  .address { position: absolute; left: 36px; top: 222px; font-size: 16px; color: var(--navy); }

  .tagline {
    position: absolute; right: 34px; top: 196px;
    font-family: "Patrick Hand", cursive;
    font-size: 20px; line-height: 22px; color: var(--navy);
    text-align: right;
  }

  .skyline-art {
    position: absolute; left: 0; right: 0; bottom: 0; height: 90px;
    background: linear-gradient(180deg, rgba(194,115,29,0) 0%, rgba(194,115,29,0.18) 60%, rgba(194,115,29,0.28) 100%);
  }
</style>
</head>
<body>
<main class="canvas">

  <section class="card card-front">
    <div class="brand-name">
      <div class="brand-title">BAYFERN VET</div>
      <div class="brand-sub">URGENT CARE</div>
    </div>
    <div class="walk-in-band">NO APPOINTMENT NECESSARY</div>
    <p class="hours"><span class="label">Hours:</span> Mon-Fri: 4PM -10PM <span class="divider">|</span> Sat-Sun- 10AM- 5PM</p>
  </section>

  <section class="card card-back">
    <h1 class="doctor-name">Dr. Elena Marsh</h1>
    <div class="brand-name">
      <div class="brand-title">BAYFERN VET</div>
      <div class="brand-sub">URGENT CARE</div>
    </div>

    <ul class="contact-list">
      <li>
        <svg viewBox="0 0 16 16" aria-hidden="true"><path d="M2 5c0-2 2-3 6-3s6 1 6 3v1h-3V5H5v1H2z M4 7h8l2 6H2z"/></svg>
        555-718-2946
      </li>
      <li>
        <svg viewBox="0 0 16 16" aria-hidden="true"><path d="M1 3h14v10H1z M2 4l6 5 6-5" stroke="#eee" stroke-width="1.2"/></svg>
        help@bayfernvet.com
      </li>
      <li>
        <svg viewBox="0 0 16 16" aria-hidden="true"><circle cx="8" cy="8" r="7"/><path d="M1 8h14M8 1v14M3 4.5h10M3 11.5h10" stroke="#eee" stroke-width="1" fill="none"/></svg>
        www.bayfernvet.com
      </li>
    </ul>
    <p class="address">4173 SE 19th Ave. OKC, OK 73958</p>

    <p class="tagline">We're here when<br>you need us</p>

    <div class="skyline-art" role="img" aria-label="Orange outline city skyline along the bottom edge"></div>
  </section>

</main>
</body>
</html>
```